Builder Website Brackwell Construction

Hi,
Brackwell Construction is a domestic builder on the Gold Coast specializing in new homes, townhouses, duplexes and high end renovations.
Brackwell Construction can make your dream new home or development a reality. Whether you already have plans or require a complete design and construct project service, Brackwell Construction will make your project a stress free experience.
We offer design, town planning, certification and construction services.

Target Market(s)

Anyone looking to build.

Industry/Entity Type

Building

Coding

Coded - Design and coding required

Font styles to use
Other font styles liked:
• Match logo

Colors

Designer to choose colors to be used in the design.

Requirements
Must have
• Attractive home page with logo etc.
• About us page
• Gallery page
• Services Page
• Contact us page

```html
<!DOCTYPE html>
<html lang="en">
<head>
<meta charset="utf-8">
<title>Brackwell Construction</title>
<link href="https://fonts.googleapis.com/css2?family=Montserrat:wght@400;500;600;700&family=Mulish:ital,wght@0,400;0,600;1,400&display=swap" rel="stylesheet">
<style>
:root{
  --navy:#0b0b3d;
  --navy-deep:#07072e;
  --grey:#ececec;
  --grey-mid:#dcdcdc;
  --cream:#f6f4f0;
  --ink:#1b1b2b;
  --body:#4a4a55;
  --white:#ffffff;
  --head:'Montserrat',Arial,sans-serif;
  --text:'Mulish',Arial,sans-serif;
}
*{box-sizing:border-box;margin:0;padding:0}
html,body{width:1200px;height:3879px;overflow:hidden}
body{position:relative;background:var(--white);font-family:var(--text);color:var(--body)}
.abs{position:absolute}
.center{left:0;width:1200px;text-align:center}
h1,h2,h3{font-family:var(--head);color:var(--ink);font-weight:600}
.btn{display:inline-block;font-family:var(--head);font-size:15px;font-weight:500;padding:0 20px;height:48px;line-height:44px;border:2px solid var(--navy);color:var(--navy);text-decoration:none}
.btn-solid{background:var(--navy);color:var(--white)}
.btn-light{border-color:var(--white);color:var(--white)}
.rule{width:70px;height:3px;background:var(--ink);margin:14px auto 0}

/* header */
.topbar{top:0;left:0;width:1200px;height:130px;background:var(--white);border-top:4px solid var(--navy);z-index:3}
.contact-pill{top:0;right:100px;height:42px;display:flex;font-size:14px}
.contact-pill span{display:flex;align-items:center;gap:8px;padding:0 22px}
.pill-mail{background:var(--grey);color:var(--ink);border-radius:0 0 0 22px}
.pill-phone{background:var(--navy);color:var(--white);border-radius:0 0 22px 0}
.nav{top:78px;right:98px;display:flex;gap:42px;font-family:var(--head);font-size:15px;font-weight:500;color:var(--ink)}
.brand{top:0;left:122px;width:186px;height:210px;background:var(--white);border-radius:0 0 93px 93px;z-index:4;text-align:center}
.brand-dot{width:78px;height:78px;border:3px solid var(--ink);border-radius:50%;margin:18px auto 8px}
.brand-name{font-family:var(--text);font-size:34px;font-weight:400;color:var(--ink);line-height:1}

/* hero */
.hero{top:130px;left:0;width:1200px;height:520px;background:linear-gradient(160deg,#b9a48a 0%,#d8c8b2 40%,#8f7a62 100%)}
.hero-title{top:265px;font-family:var(--head);font-size:50px;font-weight:700;color:var(--white);letter-spacing:1px}
.hero-sub{top:346px;font-family:var(--head);font-size:32px;font-weight:500;color:var(--white)}
.hero-btn{top:428px}
.dots{display:flex;gap:6px;justify-content:center}
.dots i{width:14px;height:14px;border-radius:50%;background:#cfcfcf;display:block}
.dots i:first-child{background:var(--white)}
.hero-dots{top:622px}

/* intro panels */
.panels{top:585px;left:0}
.panel-copy{width:480px;font-size:14px;line-height:23px}
.panel h2{font-size:30px;margin:20px 0 14px}
.panel-left{top:690px;left:98px}
.panel-right{top:690px;left:622px;text-align:right;color:#cfd0e4}
.panel-right h2{color:var(--white)}
.panel-icon{width:74px;height:62px}
.panel-right .panel-icon{margin-left:auto}
.panel-left .btn{margin-top:24px;height:46px;line-height:42px}
.panel-right .btn{margin-top:24px;height:46px;line-height:42px}

/* about */
.about-dot{top:1032px;left:577px;width:46px;height:46px;border:2px solid var(--ink);border-radius:50%}
.about-kicker{top:1098px;font-family:var(--head);font-size:21px;font-weight:600;color:var(--ink)}
.about-title{top:1133px;font-size:29px}
.about-copy{top:1195px;left:110px;width:980px;text-align:center;font-size:14px;line-height:25px}
.about-btn{top:1318px}

/* services */
.services-band{top:1440px;left:0;width:1200px;height:760px}
.services-title{top:1545px;font-size:30px}
.svc{font-family:var(--head);font-weight:600;color:var(--ink);text-align:center;font-size:19px}
.svc-small{background:var(--grey-mid);border-top:3px solid var(--navy);padding-top:28px}
.svc-small svg{display:block;margin:0 auto 16px}
.svc-main{top:1672px;left:300px;width:597px;height:332px;background:var(--navy);color:var(--white);padding-top:38px}
.svc-main h3{color:var(--white);font-size:28px;margin:18px 0 16px}
.svc-main p{font-family:var(--text);font-weight:400;font-size:20px;line-height:30px;color:#e3e3f0}
.svc-active{background:var(--navy);color:var(--white)}

/* works */
.works-title{top:2258px;font-size:30px}
.tabs{top:2385px;left:0;width:1200px;display:flex;gap:14px;justify-content:center}
.tab{width:214px;height:52px;border:2px solid var(--ink);border-radius:26px;font-family:var(--head);font-size:15px;font-weight:600;color:var(--ink);display:flex;align-items:center;justify-content:center}
.tab-on{background:var(--navy);border-color:var(--navy);color:var(--white)}
.photo{border:3px solid var(--white);box-shadow:0 0 0 1px #bbb}

/* testimonials */
.testi-title{top:3068px;font-size:30px;color:var(--white)}
.testi-title .rule{background:var(--white)}
.quote-mark{top:3138px;font-family:var(--head);font-size:60px;color:var(--white);line-height:1}
.testi-copy{top:3205px;left:220px;width:760px;text-align:center;font-style:italic;font-size:15px;line-height:27px;color:var(--white)}
.testi-dots{top:3290px}

/* contact */
.contact-title{top:3448px;font-size:30px}
.contact-copy{top:3540px;left:160px;width:880px;text-align:center;font-size:15px;line-height:27px;color:var(--ink)}
.contact-row{top:3628px;left:0;width:1200px;display:flex;justify-content:center;gap:34px;font-size:19px;color:var(--ink)}
.contact-row span{display:flex;align-items:center;gap:14px}
.ring{width:44px;height:44px;border:2px solid var(--ink);border-radius:50%;display:flex;align-items:center;justify-content:center}
.footer-nav{top:3728px;left:0;width:1200px;display:flex;justify-content:center;gap:44px;font-size:17px;color:var(--ink)}
.footer-line{top:3792px;left:98px;width:1004px;height:1px;background:#9a9a9a}
.copyright{top:3818px;font-size:15px;color:var(--ink)}
</style>
</head>
<body>

<header>
  <div class="abs topbar"></div>
  <div class="abs contact-pill" style="z-index:5">
    <span class="pill-mail"><svg width="14" height="11" viewBox="0 0 14 11"><rect x="0.5" y="0.5" width="13" height="10" fill="none" stroke="#1b1b2b"/><path d="M1 1l6 5 6-5" fill="none" stroke="#1b1b2b"/></svg>info@brackwellconstructions.com</span>
    <span class="pill-phone"><svg width="12" height="12" viewBox="0 0 12 12"><path d="M2 1l2 0 1 3-1.5 1a7 7 0 0 0 3.5 3.5L8 7l3 1 0 2c-5 1-10-4-9-9z" fill="#fff"/></svg>Phone: 123 456 7890</span>
  </div>
  <nav class="abs nav" style="z-index:5">
    <span>HOME</span><span>ABOUT US</span><span>GALLERY</span><span>SERVICES</span><span>CONTACT US</span>
  </nav>
  <div class="abs brand">
    <div class="brand-dot"></div>
    <div class="brand-name">Brackwell</div>
  </div>
</header>

<section>
  <div class="abs hero" role="img" aria-label="Interior of a kitchen under construction with unfinished cabinets and a ladder"></div>
  <h1 class="abs center hero-title">WELCOME TO BRACKWELL</h1>
  <div class="abs center hero-sub">Construction</div>
  <div class="abs center hero-btn"><span class="btn btn-light">Read More</span></div>
</section>

<section>
  <svg class="abs panels" width="1200" height="520" viewBox="0 0 1200 520">
    <polygon points="0,5 600,100 600,410 0,500" fill="#ececec"/>
    <polygon points="600,100 1200,5 1200,500 600,410" fill="#0b0b3d"/>
    <polygon points="0,0 600,95 1200,0 1200,5 600,100 0,5" fill="#ffffff"/>
  </svg>
  <div class="abs center hero-dots dots"><i></i><i></i><i></i><i></i><i></i></div>

  <div class="abs panel panel-left">
    <svg class="panel-icon" viewBox="0 0 74 62"><rect x="4" y="20" width="66" height="38" rx="6" fill="#0b0b3d"/><rect x="24" y="6" width="26" height="16" rx="3" fill="none" stroke="#0b0b3d" stroke-width="5"/><rect x="4" y="34" width="66" height="4" fill="#ececec"/></svg>
    <h2>Brackwell Construction</h2>
    <p class="panel-copy">Nemo enim ipsam voluptatem quia voluptas sit aspernatur aut odit aut fugit, sed quia consequuntur magni dolores eos qui ratione voluptatem sequi nesciunt.</p>
    <span class="btn">Read More</span>
  </div>
  <div class="abs panel panel-right">
    <svg class="panel-icon" viewBox="0 0 74 62"><path d="M10 38a27 27 0 0 1 54 0z" fill="#fff"/><rect x="6" y="38" width="62" height="6" fill="#fff"/><rect x="33" y="6" width="8" height="18" fill="#0b0b3d"/><path d="M20 48h34l-6 12h-22z" fill="#fff"/></svg>
    <h2>Domestic Builder</h2>
    <p class="panel-copy" style="margin-left:auto">Nemo enim ipsam voluptatem quia voluptas sit aspernatur aut odit aut fugit, sed quia consequuntur magni dolores eos qui ratione voluptatem sequi nesciunt.</p>
    <span class="btn btn-light">Read More</span>
  </div>
</section>

<section>
  <div class="abs about-dot"></div>
  <div class="abs center about-kicker">About</div>
  <h2 class="abs center about-title">Brackwell Constructions</h2>
  <p class="abs about-copy">Nemo enim ipsam voluptatem quia voluptas sit aspernatur aut odit aut fugit, sed quia consequuntur magni dolores eos qui ratione voluptatem sequi nesciunt. Neque porro quisquam est, qui dolorem ipsum quia dolor sit amet, consectetur, adipisci velit, sed quia non numquam eius modi tempora incidunt ut labore et dolore magnam aliquam quaerat voluptatem.</p>
  <div class="abs center about-btn"><span class="btn btn-solid">Read More</span></div>
</section>

<section>
  <svg class="abs services-band" viewBox="0 0 1200 760" role="img" aria-label="Faint city skyline and architectural sketch behind the services">
    <defs><linearGradient id="bandFade" x1="0" y1="0" x2="0" y2="1"><stop offset="0" stop-color="#f6f4f0"/><stop offset="0.5" stop-color="#efebe4"/><stop offset="1" stop-color="#f6f4f0"/></linearGradient></defs>
    <polygon points="0,140 600,12 1200,140 1200,630 600,745 0,630" fill="url(#bandFade)"/>
    <polyline points="0,138 600,10 1200,138" fill="none" stroke="#0b0b3d" stroke-width="4"/>
    <polyline points="0,632 600,748 1200,632" fill="none" stroke="#0b0b3d" stroke-width="6"/>
  </svg>
  <h2 class="abs center services-title">OUR SERVICES<div class="rule"></div></h2>

  <div class="abs svc svc-small" style="top:1668px;left:98px;width:192px;height:168px">
    <svg width="58" height="50" viewBox="0 0 58 50"><rect x="3" y="3" width="52" height="34" fill="#1b1b2b"/><rect x="9" y="9" width="40" height="22" fill="#dcdcdc"/><rect x="25" y="37" width="8" height="8" fill="#1b1b2b"/><rect x="15" y="45" width="28" height="4" fill="#1b1b2b"/></svg>
    DESIGN
  </div>
  <div class="abs svc svc-small" style="top:1842px;left:98px;width:192px;height:162px">
    <svg width="58" height="50" viewBox="0 0 58 50"><rect x="22" y="4" width="22" height="44" fill="#1b1b2b"/><rect x="8" y="24" width="16" height="24" fill="#1b1b2b"/><g fill="#dcdcdc"><rect x="27" y="10" width="5" height="5"/><rect x="35" y="10" width="5" height="5"/><rect x="27" y="20" width="5" height="5"/><rect x="35" y="20" width="5" height="5"/><rect x="12" y="30" width="5" height="5"/></g></svg>
    TOWN PLANNING
  </div>
  <div class="abs svc svc-main">
    <svg width="92" height="86" viewBox="0 0 92 86"><path d="M14 58a30 30 0 0 1 60 0z" fill="none" stroke="#fff" stroke-width="5"/><rect x="8" y="58" width="72" height="8" fill="#fff"/><path d="M58 8l14 0 6 6-16 16-8-8z" fill="#fff"/></svg>
    <h3>CONSTRUCTION</h3>
    <p>Sed ut perspiciatis unde omnis iste natus<br>error sit voluptatem.</p>
  </div>
  <div class="abs svc svc-small" style="top:1668px;left:910px;width:190px;height:168px;font-size:17px">
    <svg width="46" height="54" viewBox="0 0 46 54"><rect x="3" y="3" width="40" height="48" fill="none" stroke="#1b1b2b" stroke-width="3"/><g stroke="#1b1b2b" stroke-width="3"><line x1="10" y1="13" x2="36" y2="13"/><line x1="10" y1="21" x2="36" y2="21"/></g><circle cx="28" cy="38" r="7" fill="none" stroke="#1b1b2b" stroke-width="3"/></svg>
    CERTIFICATION
  </div>
  <div class="abs svc svc-small svc-active" style="top:1842px;left:910px;width:190px;height:162px;font-size:17px">
    <svg width="58" height="50" viewBox="0 0 58 50"><path d="M8 34a20 20 0 0 1 40 0z" fill="none" stroke="#fff" stroke-width="4"/><rect x="4" y="34" width="48" height="6" fill="#fff"/><path d="M38 4l10 0 4 4-11 11-6-6z" fill="#fff"/></svg>
    CONSTRUCTION
  </div>
</section>

<section>
  <h2 class="abs center works-title">OUR CONSTRUCTION WORKS</h2>
  <div class="abs tabs">
    <div class="tab tab-on">TOWNHOUSES</div>
    <div class="tab">DUPLEXES</div>
    <div class="tab">HIGH END RENOVATIONS</div>
  </div>
  <div class="abs" style="top:2496px;left:98px;width:437px;height:336px;background:var(--grey-mid)"></div>
  <div class="abs" style="top:2496px;left:667px;width:432px;height:336px;background:var(--navy)"></div>
  <div class="abs photo" style="top:2534px;left:129px;width:440px;height:260px;background:linear-gradient(180deg,#b9cde0 0%,#a7573f 35%,#8c4431 75%,#9a9a94 100%)" role="img" aria-label="Row of red brick townhouses along a street"></div>
  <div class="abs photo" style="top:2534px;left:631px;width:437px;height:262px;background:linear-gradient(180deg,#c9d6e2 0%,#9a6a4e 40%,#6d5648 75%,#8d8a84 100%)" role="img" aria-label="Modern duplex homes with timber cladding"></div>
  <svg class="abs" style="top:2632px;left:530px" width="140" height="66" viewBox="0 0 140 66">
    <path d="M70 0h-37a33 33 0 0 0 0 66h37z" fill="#0b0b3d"/>
    <path d="M70 0h37a33 33 0 0 1 0 66h-37z" fill="#fff"/>
    <polyline points="52,20 40,33 52,46" fill="none" stroke="#fff" stroke-width="3"/>
    <polyline points="88,20 100,33 88,46" fill="none" stroke="#0b0b3d" stroke-width="3"/>
  </svg>
</section>

<section>
  <svg class="abs" style="top:2890px;left:0" width="1200" height="590" viewBox="0 0 1200 590" role="img" aria-label="Dark navy-tinted photo of a carpenter working on timber">
    <defs><linearGradient id="testiBg" x1="0" y1="0" x2="1" y2="1"><stop offset="0" stop-color="#1a1a4e"/><stop offset="0.6" stop-color="#242452"/><stop offset="1" stop-color="#121238"/></linearGradient></defs>
    <polygon points="0,0 1200,0 1200,475 600,395 0,475" fill="url(#testiBg)"/>
    <polygon points="0,0 1200,0 1200,22 600,95 0,22" fill="#0b0b3d"/>
    <polyline points="0,32 600,108 1200,32" fill="none" stroke="#fff" stroke-width="5"/>
    <polygon points="0,475 600,395 1200,475 1200,590 0,590" fill="#fff"/>
    <polygon points="0,460 600,380 1200,460 1200,478 600,400 0,478" fill="#0b0b3d"/>
  </svg>
  <h2 class="abs center testi-title">OUR TESTIMONIALS<div class="rule"></div></h2>
  <div class="abs center quote-mark">&ldquo;</div>
  <p class="abs testi-copy">Nemo enim ipsam voluptatem quia voluptas sit aspernatur aut odit aut fugit, sed quia consequun tur magni dolores eos qui ratione voluptatem sequi nesciunt.</p>
  <div class="abs center testi-dots dots"><i></i><i></i><i></i><i></i><i></i></div>
</section>

<footer>
  <h2 class="abs center contact-title">CONTACT US<div class="rule"></div></h2>
  <p class="abs contact-copy">Nemo enim ipsam voluptatem quia voluptas sit aspernatur aut odit aut fugit, sed quia consequuntur magni dolores eos qui ratione voluptatem sequi nesciunt.</p>
  <div class="abs contact-row">
    <span><span class="ring"><svg width="18" height="18" viewBox="0 0 12 12"><path d="M2 1l2 0 1 3-1.5 1a7 7 0 0 0 3.5 3.5L8 7l3 1 0 2c-5 1-10-4-9-9z" fill="none" stroke="#1b1b2b"/></svg></span>123 456 7890</span>
    <span><span class="ring"><svg width="18" height="14" viewBox="0 0 14 11"><rect x="0.5" y="0.5" width="13" height="10" fill="none" stroke="#1b1b2b"/><path d="M1 1l6 5 6-5" fill="none" stroke="#1b1b2b"/></svg></span>info@brackwellconstructions.com</span>
  </div>
  <nav class="abs footer-nav">
    <span>Home</span><span>|</span><span>About Us</span><span>|</span><span>Gallery</span><span>|</span><span>Services</span><span>|</span><span>Contact Us</span>
  </nav>
  <div class="abs footer-line"></div>
  <div class="abs center copyright">Copyrights @ 2018 Brackwell Constructions. All Rights Reserved.</div>
</footer>

</body>
</html>
```